Store Signage for New Location

I need a banner for my new location. It needs to communicate 1: our name, 2: our phone number 3: our message. This is going to be a 7 foot wide banner that is 4 feet tall. It needs to be a very high resolution design so it prints properly.

Our phone number is (555) 418-2097

Our Message: The HONEST alternative to the dealer.

Or: Your Honest Auto Service Center

"Honest" is our key word here.
Updates

Target Market(s)

Drive-by traffic.

Industry/Entity Type

Auto Repair

Requirements
Must have
• The name of our business: Fair Lane Auto Repair
• Our phone number: (555) 418-2097
• Our message: The HONEST alternative to the dealership.
• or: Your Honest Service Center
Nice to have
• I really just need a clean layout using the uploaded logo and font. It needs to be highly visible as a sign that is seen by drive-by traffic.
• I'd like the color scheme to be the same as what I have, however, you're more than welcome to add detail and color as needed.

```html
<!DOCTYPE html>
<html lang="en">
<head>
<meta charset="utf-8">
<title>Fair Lane Auto Repair – Store Banner</title>
<link rel="stylesheet" href="https://fonts.googleapis.com/css2?family=Graduate&family=Oswald:wght@700&family=Roboto+Condensed:wght@800&family=Zilla+Slab:ital,wght@1,700&display=swap">
<style>
  :root {
    --page-bg: #e9ebee;
    --banner-black: #0b0b0b;
    --banner-white: #ffffff;
    --ink: #111111;
    --phone-top: #ffffff;
    --phone-bottom: #a9a9ab;
  }
  html, body {
    margin: 0;
    width: 1200px;
    height: 962px;
    overflow: hidden;
    background: var(--page-bg);
  }
  .banner {
    position: absolute;
    left: 40px;
    top: 161px;
    width: 1120px;
    height: 640px;
    background: var(--banner-black);
    overflow: hidden;
  }
  .banner__header-band {
    position: absolute;
    inset: 0;
    width: 1120px;
    height: 640px;
  }
  .brand {
    position: absolute;
    left: 90px;
    top: 78px;
    display: flex;
    align-items: center;
    gap: 26px;
  }
  .brand__dot {
    width: 86px;
    height: 86px;
    border-radius: 50%;
    background: var(--ink);
  }
  .brand__name {
    font-family: "Roboto Condensed", sans-serif;
    font-weight: 800;
    font-size: 66px;
    color: var(--ink);
    letter-spacing: 0.5px;
  }
  .tagline {
    position: absolute;
    left: 90px;
    top: 340px;
    width: 950px;
    font-family: "Graduate", serif;
    font-size: 50px;
    color: var(--banner-white);
    white-space: nowrap;
  }
  .tagline__keyword {
    font-family: "Zilla Slab", serif;
    font-style: italic;
    font-weight: 700;
    font-size: 76px;
    letter-spacing: 1px;
  }
  .phone {
    position: absolute;
    left: 90px;
    top: 430px;
    font-family: "Oswald", sans-serif;
    font-weight: 700;
    font-size: 150px;
    line-height: 1;
    letter-spacing: 2px;
    background: linear-gradient(180deg, var(--phone-top) 30%, var(--phone-bottom) 100%);
    -webkit-background-clip: text;
    background-clip: text;
    color: transparent;
  }
</style>
</head>
<body>
  <main class="banner">
    <svg class="banner__header-band" viewBox="0 0 1120 640" aria-hidden="true">
      <path d="M0 0 H1120 V235 Q620 330 0 275 Z" fill="var(--banner-white)"/>
    </svg>
    <div class="brand">
      <span class="brand__dot"></span>
      <span class="brand__name">Fair Lane Auto Repair</span>
    </div>
    <p class="tagline" style="margin:0">YOUR <span class="tagline__keyword">HONEST</span> SERVICE CENTER</p>
    <p class="phone" style="margin:0">(555) 418-2097</p>
  </main>
</body>
</html>
```